Chiropractic healthcare group business card

We are a Portland Oregon based chiropractic healthcare group. Looking for a new business card design. Something cutting edge, that shows off our new logo and tag line.Use either of the attached logos.Our tag line = "Who would you be without pain?"I'm open to about anything, impress me!!
Target Market(s)
Chiropractic patients - Auto injury, back pain, sports injuries, neck , shoulder, hip, knee, ankle pain.
Industry/Entity Type
Chiropractic
Contact Information for Business Card
Dr. Bram Holtvick, D.C.
Clinic name - Fernway Chiropractic
2 clinics
location #1
20418 NW Marwick Road
Suite B
North Plains, OR 97133
Location #2
13529 SE Calloway Street
Portland OR 97236
Main phone line 971.555.0143
website : www.FernwayClinics.example
Tag line "Who would you be without pain?"
Colors
Designer to choose colors to be used in the design.
Requirements
Must have
- Use the logo colors -- Want the orange color to be a TRUE orange.
- Both clinic address
- phone number
- website
- personal email - b.holtvick@ReliefBeginsHere.example
- tag line - "Who would you be without pain?"

```html
<!DOCTYPE html>
<html lang="en">
<head>
<meta charset="utf-8">
<title>Fernway Chiropractic – Business Card</title>
<link href="https://fonts.googleapis.com/css2?family=Arimo:ital,wght@0,400;0,600;0,700;1,400;1,700&display=swap" rel="stylesheet">
<style>
  :root {
    --orange: #f59a29;
    --slate: #616161;
    --ink: #5d5d5e;
    --white: #ffffff;
    --page: #ffffff;
    --edge: #b9b9b9;
    --edge-warm: #b08a6a;
  }
  * { margin: 0; padding: 0; box-sizing: border-box; }
  html, body {
    width: 1200px; height: 420px; overflow: hidden;
    background: var(--page);
    font-family: "Arimo", Arial, sans-serif;
  }
  .canvas { position: relative; width: 1200px; height: 420px; }

  .card {
    position: absolute; width: 480px; height: 300px;
    background: var(--white); overflow: hidden;
  }
  .card--front { left: 71px; top: 60px; border: 1px solid var(--edge); }
  .card--back { left: 637px; top: 56px; border: 1px solid var(--edge-warm); }
  .card__shapes { position: absolute; inset: 0; width: 100%; height: 100%; }

  .tagline {
    position: absolute; left: 60px; top: 120px;
    font-size: 18.5px; font-style: italic; color: var(--ink);
    letter-spacing: 0.2px; white-space: nowrap;
  }
  .tagline__key { font-weight: 700; color: var(--white); font-size: 21px; }
  .tagline__mark { font-weight: 700; color: var(--ink); font-size: 21px; }

  .front-name {
    position: absolute; left: 304px; top: 186px;
    display: flex; align-items: center; gap: 8px;
  }
  .front-name__dot { width: 12px; height: 12px; background: var(--white); }
  .front-name__text {
    font-size: 32px; font-weight: 700; color: var(--ink); letter-spacing: 0.5px;
  }

  .brand {
    position: absolute; left: 6px; top: 50px; width: 180px;
    display: flex; flex-direction: column; align-items: center;
  }
  .brand__dot { width: 14px; height: 14px; background: var(--orange); margin-bottom: 24px; }
  .brand__name {
    font-size: 27px; font-weight: 700; color: var(--ink);
    letter-spacing: 2px; line-height: 1; white-space: nowrap;
  }
  .brand__sub {
    margin-top: 12px;
    font-size: 11.5px; font-weight: 700; color: var(--ink);
    letter-spacing: 2.2px; line-height: 1; white-space: nowrap;
  }

  .contact { position: absolute; left: 258px; top: 84px; color: var(--white); }
  .contact__name { font-size: 17px; font-weight: 700; color: var(--orange); white-space: nowrap; }
  .contact__cred { font-size: 12px; font-weight: 400; }
  .contact__clinic { font-size: 13px; font-style: italic; margin-top: 4px; }
  .contact__list { list-style: none; margin-top: 20px; }
  .contact__item {
    position: relative; padding-left: 17px;
    font-size: 12.8px; line-height: 15.6px; letter-spacing: 0.3px; white-space: nowrap;
  }
  .contact__item + .contact__item { margin-top: 8px; }
  .contact__item--tight { margin-top: 3px !important; }
  .contact__icon { position: absolute; left: 0; top: 1px; width: 12px; height: 13px; }
</style>
</head>
<body>
<main class="canvas">

  <section class="card card--front" aria-label="Card front">
    <svg class="card__shapes" viewBox="0 0 480 300" preserveAspectRatio="none" aria-hidden="true">
      <polygon points="0,0 456,0 284,300 0,300" fill="var(--orange)"/>
    </svg>
    <p class="tagline">Who would you be without <span class="tagline__key">pain</span><span class="tagline__mark">?</span></p>
    <div class="front-name">
      <span class="front-name__dot"></span>
      <span class="front-name__text">Fernway</span>
    </div>
  </section>

  <section class="card card--back" aria-label="Card back">
    <svg class="card__shapes" viewBox="0 0 480 300" preserveAspectRatio="none" aria-hidden="true">
      <polygon points="260,0 266,0 95,300 89,300" fill="var(--orange)"/>
      <polygon points="266,0 480,0 480,300 95,300" fill="var(--slate)"/>
    </svg>

    <div class="brand">
      <span class="brand__dot"></span>
      <p class="brand__name">Fernway</p>
      <p class="brand__sub">CHIROPRACTIC</p>
    </div>

    <div class="contact">
      <p class="contact__name">Dr. Bram Holtvick, <span class="contact__cred">D.C.</span></p>
      <p class="contact__clinic">Fernway Chiropractic</p>
      <ul class="contact__list">
        <li class="contact__item">
          <svg class="contact__icon" viewBox="0 0 12 14" aria-hidden="true"><path d="M6 0a5 5 0 0 0-5 5c0 3.5 5 9 5 9s5-5.5 5-9a5 5 0 0 0-5-5zm0 7.2A2.2 2.2 0 1 1 6 2.8a2.2 2.2 0 0 1 0 4.4z" fill="var(--orange)"/></svg>
          20418 NW Marwick Road<br>Suite B<br>North Plains, OR 97133
        </li>
        <li class="contact__item">
          <svg class="contact__icon" viewBox="0 0 12 14" aria-hidden="true"><path d="M6 0a5 5 0 0 0-5 5c0 3.5 5 9 5 9s5-5.5 5-9a5 5 0 0 0-5-5zm0 7.2A2.2 2.2 0 1 1 6 2.8a2.2 2.2 0 0 1 0 4.4z" fill="var(--orange)"/></svg>
          13529 SE Calloway Street<br>Portland OR 97236
        </li>
        <li class="contact__item">
          <svg class="contact__icon" viewBox="0 0 12 12" aria-hidden="true"><path d="M2.4 0.6l1.8-.3 1.2 2.7-1.2 1a6.5 6.5 0 0 0 3.6 3.6l1-1.2 2.7 1.2-.3 1.8c-.2.9-1 1.4-1.9 1.3A9.5 9.5 0 0 1 1.1 2.5C1 1.6 1.5.8 2.4.6z" fill="var(--orange)"/></svg>
          971.555.0143
        </li>
        <li class="contact__item contact__item--tight">
          <svg class="contact__icon" viewBox="0 0 12 12" aria-hidden="true"><circle cx="6" cy="6" r="5.2" fill="none" stroke="var(--orange)" stroke-width="1.4"/><path d="M3 3.2c1 .2 1.6.8 1.4 1.8-.2.8.6 1.2 1.2 1.6.5.4.2 1.4-.2 2.3M7.6 1.4c-.3.9.2 1.5 1 1.6.9.1 1.4.8 1.2 1.6" fill="none" stroke="var(--orange)" stroke-width="1.1"/></svg>
          www.FernwayClinics.example
        </li>
      </ul>
    </div>
  </section>

</main>
</body>
</html>
```